Updated Stationary needed using new logo for Hair Tissue Mineral Analysis Company

Simple stationary design needed using new logo!
1. 8.5" x 11" Letterhead with company information listed below
2. 8.5" x 11" Design with Footer only with logo and information for print materials
3. 5.5" x 8.5" letterhead design
4. 4.125" x 9.5" Business envelope (#10 envelope) with address
5. 4.125" x 9.5" Business envelope with clear window (#10 envelope) with address
6. 6.5" x 9.5" envelope (6 3/4 Booklet envelope) with address
7. 10" x 13" Open End envelope
Address:
4817 N. Corwin Street
Corwin Falls, AZ 86014
Phone:
(555)-417-3926
Website:
www.pexumor.com
Email:
information@pexumor.com
Updates
Need extra days to review
Focused on completing other projects first
Look and feel
Each slider illustrates characteristics of the customer's brand and the style your logo design should communicate.

```html
<!DOCTYPE html>
<html lang="en">
<head>
<meta charset="utf-8">
<title>Pexumor Labs Letterhead</title>
<link rel="stylesheet" href="https://fonts.googleapis.com/css2?family=Mulish:wght@400;600;700&display=swap">
<style>
  :root {
    --backdrop: #e0e0e0;
    --paper: #ffffff;
    --brand-blue: #2c559c;
    --brand-orange: #f48a25;
    --ink: #2b2b2b;
    --muted: #555555;
    --sig-grey: #dcdcdc;
  }
  * { margin: 0; padding: 0; box-sizing: border-box; }
  html, body { width: 1200px; height: 1200px; overflow: hidden; }
  body { background: var(--backdrop); font-family: "Mulish", sans-serif; position: relative; }

  .letterhead {
    position: absolute; left: 222px; top: 76px; width: 698px; height: 1046px;
    background: var(--paper);
    box-shadow: 6px 8px 14px rgba(0,0,0,0.18);
    overflow: hidden;
  }
  .brand {
    position: absolute; left: 0; right: 0; top: 56px;
    display: flex; justify-content: center; align-items: center; gap: 10px;
  }
  .brand-dot { width: 16px; height: 16px; border-radius: 50%; background: var(--brand-orange); }
  .brand-name { font-size: 30px; font-weight: 700; color: var(--brand-blue); letter-spacing: 0.5px; }

  .salutation {
    position: absolute; left: 53px; top: 200px;
    font-size: 23px; font-weight: 700; color: var(--brand-blue);
  }
  .letter-body {
    position: absolute; left: 51px; top: 252px; width: 584px;
    font-size: 17.4px; line-height: 26px; color: var(--ink);
  }
  .letter-body p + p { margin-top: 26px; }
  .line {
    display: block; white-space: nowrap;
    text-align: justify; text-align-last: justify;
  }
  .line.end { text-align-last: left; }
  .line.indent { padding-left: 4px; }

  .contact {
    position: absolute; left: 51px; top: 896px;
    list-style: none; font-size: 17.6px; color: var(--ink); line-height: 19px;
  }
  .contact li { display: flex; align-items: flex-start; gap: 6px; margin-bottom: 6px; }
  .contact svg { flex: none; margin-top: 1px; }

  .signoff { position: absolute; left: 482px; top: 851px; color: var(--muted); }
  .signoff-name { font-size: 11px; }
  .signoff-title { font-size: 8.5px; margin-top: 3px; }
  .signature {
    position: absolute; left: 468px; top: 866px; width: 170px; height: 104px;
    background: radial-gradient(ellipse at 55% 55%, var(--sig-grey) 0%, rgba(220,220,220,0) 70%);
    opacity: 0.7;
  }

  .footer-band { position: absolute; left: 0; bottom: 0; width: 698px; height: 50px; }
  .website {
    position: absolute; right: 37px; bottom: 9px;
    font-size: 23px; color: #ffffff; letter-spacing: 1.2px;
  }
</style>
</head>
<body>
  <main class="letterhead">
    <header class="brand">
      <span class="brand-dot"></span>
      <span class="brand-name">Pexumor Labs</span>
    </header>

    <h1 class="salutation">Dear Mr. Reyes,</h1>

    <section class="letter-body">
      <p>
        <span class="line">Lorem ipsum dolor sit amet, consectetuer adipiscing elit, sed diam</span>
        <span class="line">nonummy nibh euismod tincidunt ut laoreet dolore magna aliquam erat</span>
        <span class="line">volutpat. Ut wisi enim ad minim veniam, quis nostrud exerci tation</span>
        <span class="line">ullamcorper suscipit lobortis nisl ut aliquip ex ea commodo consequat.</span>
        <span class="line end">Duis autem vel eum iriure dolor in</span>
        <span class="line indent">hendrerit in vulputate velit esse molestie consequat, vel illum dolore eu</span>
        <span class="line">feugiat nulla facilisis at vero eros et accumsan et iusto odio dignissim qui</span>
        <span class="line">blandit praesent luptatum zzril delenit augue duis dolore te feugait nulla</span>
        <span class="line end">facilisi.</span>
      </p>
      <p>
        <span class="line">Lorem ipsum dolor sit amet, cons ectetuer adipiscing elit, sed diam</span>
        <span class="line">nonummy nibh euismod tincidunt ut laoreet dolore magna aliquam erat</span>
        <span class="line">volutpat. Ut wisi Lorem ipsum dolor sit amet, consectetuer adipiscing</span>
        <span class="line">elit, sed diam nonummy nibh euismod tincidunt ut laoreet dolore magna</span>
        <span class="line">aliquam erat volutpat. Ut wisi enim ad minim veniam, quis nostrud exerci</span>
        <span class="line">tation ullamcorper suscipit lobortis nisl ut aliquip ex ea commodo conse-</span>
        <span class="line">quat. Duis autem vel eum iriure dolor in hendrerit in vulputate velit esse</span>
        <span class="line">molestie consequat,Lorem ipsum dolor sit amet, cons ectetuer adipisc-</span>
        <span class="line">ing elit, sed diam nonummy nibh euismod tincidunt ut laoreet dolore</span>
        <span class="line end">magna aliquam erat volutpat.</span>
      </p>
    </section>

    <ul class="contact">
      <li>
        <svg width="18" height="18" viewBox="0 0 24 24" aria-hidden="true"><path fill="var(--brand-orange)" d="M6.6 10.8a15.1 15.1 0 0 0 6.6 6.6l2.2-2.2c.3-.3.7-.4 1-.2 1.1.4 2.3.6 3.6.6.6 0 1 .4 1 1V20c0 .6-.4 1-1 1A17 17 0 0 1 3 4c0-.6.4-1 1-1h3.5c.6 0 1 .4 1 1 0 1.3.2 2.5.6 3.6.1.3 0 .7-.2 1z"/></svg>
        <span>(555)-417-3926</span>
      </li>
      <li>
        <svg width="18" height="18" viewBox="0 0 24 24" aria-hidden="true"><path fill="var(--brand-orange)" d="M2 5h20v14H2z"/><path fill="none" stroke="#fff" stroke-width="1.6" d="M2 5l10 8 10-8M2 19l7-7M22 19l-7-7"/></svg>
        <span>information@pexumor.com</span>
      </li>
      <li>
        <svg width="18" height="22" viewBox="0 0 24 30" aria-hidden="true"><path fill="none" stroke="var(--brand-orange)" stroke-width="3.2" d="M12 28S3 17 3 11a9 9 0 0 1 18 0c0 6-9 17-9 17z"/><circle cx="12" cy="11" r="3.4" fill="none" stroke="var(--brand-orange)" stroke-width="2.6"/></svg>
        <span>4817 N. Corwin Street<br>Corwin Falls, AZ 86014</span>
      </li>
    </ul>

    <div class="signoff">
      <div class="signoff-name">Dana Reyes</div>
      <div class="signoff-title">Office Manager</div>
    </div>
    <div class="signature" role="img" aria-label="Handwritten signature of the office manager"></div>

    <svg class="footer-band" viewBox="0 0 698 50" aria-hidden="true">
      <path fill="var(--brand-orange)" d="M0 19 H388 C393 19 397 18 402 16.5 L396 24 H0 Z"/>
      <path fill="var(--brand-blue)" d="M0 27 H352 C385 27 395 22 410 15 C430 6 450 4 478 4 H698 V50 H0 Z"/>
    </svg>
    <div class="website">www.pexumor.com</div>
  </main>
</body>
</html>
```